Face cream packaging | Cosmetic start-up

This project is about creating design proposals for two different types of packaging. Once to a cream jar made of glass and once to a jar made of plastic.
Three different designs must be created for each type of jar. Later, the different packaging will be used as customization options in an online store for cosmetics.

- The packaging variant made of glass should have color gradients. Three different shades are to be chosen. (Preferably with the primary colors red, blue and green). Note: The designer can create other proposals at will if he has better ideas. The logo must be included in some form. (Link to manufacturer description: https://catalogue.valdorpackaging.com/en/portals/valdorpackaging/assets/12667188/lou-50-ml/)

- With the plastic type of packaging, the designer has a lot of freedom to design. The only requirement is that the design must be artistic. It doesn't matter whether abstract patterns, geometric figures, mandalas or just a basic color is chosen. The main thing is that the packaging inspires. The logo must be included in some form. (Link to manufacturer description: https://catalogue.valdorpackaging.com/en/portals/valdorpackaging/assets/12667181/edda-50-ml/)

Thank you in advance for your work and best regards
Olaf

Target Market(s)

Young people with an affinity for social media and the web. Focus is on the female clientele.

Industry/Entity Type

Cosmetics

Font styles to use
Script

Colors
eea4c8
f59195
85cae6
cadf82

Requirements
Must have
• The logo must be included in some form. (PNG-File attached)
Nice to have
• Other types of packaging (can shape, packaging material)

```html
<!DOCTYPE html>
<html lang="en">
<head>
<meta charset="utf-8">
<title>Facial Cream Labels</title>
<link href="https://fonts.googleapis.com/css2?family=Quicksand:wght@300;500&display=swap" rel="stylesheet">
<style>
  :root {
    --page: #ffffff;
    --panel: #f1f1f2;
    --silver: #9a9a9c;
    --ink: #2c2c2e;
    --rose-a: #c77bc6;
    --rose-b: #e0649a;
    --rose-c: #c7304f;
    --sea-a: #5fb5ab;
    --sea-b: #3cbfd2;
    --sea-c: #2683b6;
    --leaf-a: #8cc249;
    --leaf-b: #4ba85a;
    --leaf-c: #2d7a4c;
  }
  html, body {
    margin: 0;
    width: 1200px;
    height: 654px;
    overflow: hidden;
    background: var(--page);
    font-family: "Quicksand", sans-serif;
  }
  .lineup {
    position: relative;
    width: 1200px;
    height: 654px;
  }
  .label {
    position: absolute;
    top: 296px;
    width: 273px;
    height: 140px;
  }
  .label--rose { left: 107px; }
  .label--sea { left: 464px; }
  .label--leaf { left: 821px; }
  .label__pattern {
    position: absolute;
    inset: 0;
  }
  .label--rose .label__pattern {
    background: linear-gradient(100deg, var(--rose-a) 0%, var(--rose-b) 45%, var(--rose-c) 100%);
  }
  .label--sea .label__pattern {
    background: linear-gradient(100deg, var(--sea-a) 0%, var(--sea-b) 50%, var(--sea-c) 100%);
  }
  .label--leaf .label__pattern {
    background: linear-gradient(100deg, var(--leaf-a) 0%, var(--leaf-b) 50%, var(--leaf-c) 100%);
  }
  .label__card {
    position: absolute;
    left: 73px;
    top: 9px;
    width: 119px;
    height: 118px;
    background: var(--panel);
    border: 2px solid var(--silver);
    color: var(--ink);
    text-align: center;
  }
  .brand {
    position: absolute;
    left: 0;
    right: 0;
    top: 17px;
    font-weight: 300;
    font-size: 15px;
    line-height: 1;
    letter-spacing: 0.3px;
  }
  .brand__rule {
    position: absolute;
    left: 22px;
    right: 12px;
    top: 44px;
    height: 1px;
    background: var(--ink);
  }
  .product {
    position: absolute;
    left: 0;
    right: 0;
    top: 72px;
    font-weight: 500;
    font-size: 7px;
    line-height: 9.5px;
    letter-spacing: 4px;
    padding-left: 4px;
  }
  .volume {
    position: absolute;
    left: 0;
    right: 0;
    top: 104px;
    font-weight: 500;
    font-size: 7px;
    line-height: 1;
  }
  .volume__mark {
    font-size: 11px;
    vertical-align: -1px;
    margin-left: 2px;
  }
</style>
</head>
<body>
  <main class="lineup">
    <section class="label label--rose">
      <div class="label__pattern" role="img" aria-label="Pink to red low-poly geometric pattern"></div>
      <div class="label__card">
        <div class="brand">Mira Bloom</div>
        <div class="brand__rule"></div>
        <div class="product">FACIAL<br>CREAM</div>
        <div class="volume">100ml<span class="volume__mark">℮</span></div>
      </div>
    </section>
    <section class="label label--sea">
      <div class="label__pattern" role="img" aria-label="Turquoise to blue low-poly geometric pattern"></div>
      <div class="label__card">
        <div class="brand">Mira Bloom</div>
        <div class="brand__rule"></div>
        <div class="product">FACIAL<br>CREAM</div>
        <div class="volume">100ml<span class="volume__mark">℮</span></div>
      </div>
    </section>
    <section class="label label--leaf">
      <div class="label__pattern" role="img" aria-label="Light to deep green low-poly geometric pattern"></div>
      <div class="label__card">
        <div class="brand">Mira Bloom</div>
        <div class="brand__rule"></div>
        <div class="product">FACIAL<br>CREAM</div>
        <div class="volume">100ml<span class="volume__mark">℮</span></div>
      </div>
    </section>
  </main>
</body>
</html>
```